Zielgruppe
Hausarztpraxis Dr. Wildhagen
Patientenbetreuung / Junge Patienten
Aufgabenstellung
Bitte Mit dem Praxis Logo. Gern auch ein Foto aus der Praxis. In den Farben der Praxis Weiß-Magenta-Grau
Es soll kein Newsletter an sich werden, sondern eine Email die die Patienten nach Ihrem Besuch in der Praxis bekommen. Dort soll dann die Suchflixseite verlinkt sein mit einem Button zum bewerten!

```html
<!DOCTYPE html>
<html lang="de">
<head>
<meta charset="utf-8">
<title>Hausarztpraxis Dr. Wildhagen – Bewertung</title>
<link rel="stylesheet" href="https://fonts.googleapis.com/css2?family=Open+Sans:wght@400;600&display=swap">
<style>
  :root {
    --magenta: #c21a58;
    --magenta-soft: rgba(200, 40, 100, 0.88);
    --pink-band: #ef6399;
    --grey-text: #5a5a5a;
    --grey-dark: #4d4d4d;
    --white: #ffffff;
    --star: #f5b800;
  }
  * { margin: 0; padding: 0; box-sizing: border-box; }
  html, body { width: 1137px; height: 1200px; overflow: hidden; background: var(--white); }
  body { position: relative; font-family: "Open Sans", Arial, sans-serif; color: var(--grey-text); }

  .practice-mark { position: absolute; top: 24px; left: 0; width: 1137px; text-align: center; }
  .practice-mark__circle {
    width: 58px; height: 58px; margin: 0 auto;
    border-radius: 50%; border: 4px solid var(--magenta);
  }
  .practice-mark__name {
    margin-top: 14px; font-size: 17px; font-weight: 600; color: var(--magenta);
    letter-spacing: 0.5px;
  }

  .hero-photo {
    position: absolute; top: 173px; left: 0; width: 1137px; height: 318px;
    background: linear-gradient(100deg, #ece9e6 0%, #f4f3f1 35%, #c9bfae 58%, #d9d6d2 75%, #b8b5b2 100%);
  }
  .hero-banner {
    position: absolute; top: 408px; left: 246px; width: 644px; height: 143px;
    background: var(--magenta-soft); color: var(--white); text-align: center;
  }
  .hero-banner__title { margin-top: 33px; font-size: 33px; font-weight: 400; line-height: 1.2; }
  .hero-banner__sub { margin-top: 9px; font-size: 14px; }

  .message {
    position: absolute; top: 598px; left: 247px; width: 643px;
    text-align: center; font-size: 13px; line-height: 18px;
  }
  .message p + p { margin-top: 18px; }

  .review-button {
    position: absolute; top: 794px; left: 450px; width: 236px; height: 39px;
    border-radius: 20px; background: var(--magenta); color: var(--white);
    font-size: 14px; text-align: center; line-height: 39px; text-decoration: underline;
  }

  .closing {
    position: absolute; top: 868px; left: 200px; width: 737px;
    text-align: center; font-size: 13px; line-height: 18px;
  }
  .closing p + p { margin-top: 18px; }

  .review-badge { position: absolute; top: 1058px; left: 478px; display: flex; align-items: flex-start; gap: 7px; }
  .review-badge__dot { width: 40px; height: 40px; margin-top: 2px; border-radius: 50%; background: #4a7de8; }
  .review-badge__label { font-size: 13px; font-weight: 600; color: var(--grey-dark); line-height: 16px; }
  .review-badge__stars { display: flex; gap: 3px; margin-top: 4px; }

  .footer-stripe { position: absolute; top: 1159px; left: 0; width: 1137px; height: 12px; background: var(--pink-band); }
  .footer-nav {
    position: absolute; top: 1171px; left: 0; width: 1137px; height: 29px;
    background: var(--magenta); color: var(--white); text-align: center;
    font-size: 13px; line-height: 29px;
  }
</style>
</head>
<body>
  <header class="practice-mark">
    <div class="practice-mark__circle"></div>
    <div class="practice-mark__name">Dr. med. Henrike Wildhagen</div>
  </header>

  <div class="hero-photo" role="img" aria-label="Foto des hellen Wartebereichs der Praxis mit weißen Stühlen, Bambusstäben und grauen Sesseln"></div>

  <section class="hero-banner">
    <h1 class="hero-banner__title">Ihre Meinung ist uns wichtig.</h1>
    <p class="hero-banner__sub">Nehmen Sie sich kurz zeit und bewerten Sie uns auf Suchflix.</p>
  </section>

  <section class="message">
    <p>Liebe Patientin, Lieber Patient,</p>
    <p>wie war Ihre Erfahrung in unserer Praxis?</p>
    <p>Wir versuchen uns ständig zu verbessern und freuen uns, wenn Sie uns ein kurzes Feedback geben würden. Es Wäre toll, wenn Sie sich kurz die Zeit nehmen um eine Bewertung bei Suchflix zu schreiben, denn damit hilfst du uns und auch anderen Patienten uns zu finden.</p>
    <p>Um Ihre Bewertung zu schreiben und abzuschicken genügt ein Klick!</p>
  </section>

  <a class="review-button" href="#">Hier bewerten</a>

  <section class="closing">
    <p>Vielen Dank im Voraus für Ihre Bewertung!<br>Bei Fragen oder falls Sie uns erneut besuchen möchten, stehen wir Ihnen gern jederzeit zur Verfügung!</p>
    <p>Melden Sie sich gern unter der 07000 - 1234 oder wieder über unseren<br>Online Terminkalender der Website.</p>
    <p>Vielen Grüße<br>Ihr Praxisteam Dr. Wildhagen</p>
  </section>

  <div class="review-badge">
    <div class="review-badge__dot"></div>
    <div>
      <div class="review-badge__label">Bewerten Sie uns<br>auf Suchflix!</div>
      <div class="review-badge__stars">
        <svg width="15" height="15" viewBox="0 0 24 24"><path fill="var(--star)" d="M12 2l3 7 7.5.6-5.7 5 1.8 7.4L12 18l-6.6 4 1.8-7.4-5.7-5L9 9z"/></svg>
        <svg width="15" height="15" viewBox="0 0 24 24"><path fill="var(--star)" d="M12 2l3 7 7.5.6-5.7 5 1.8 7.4L12 18l-6.6 4 1.8-7.4-5.7-5L9 9z"/></svg>
        <svg width="15" height="15" viewBox="0 0 24 24"><path fill="var(--star)" d="M12 2l3 7 7.5.6-5.7 5 1.8 7.4L12 18l-6.6 4 1.8-7.4-5.7-5L9 9z"/></svg>
        <svg width="15" height="15" viewBox="0 0 24 24"><path fill="var(--star)" d="M12 2l3 7 7.5.6-5.7 5 1.8 7.4L12 18l-6.6 4 1.8-7.4-5.7-5L9 9z"/></svg>
        <svg width="15" height="15" viewBox="0 0 24 24"><path fill="var(--star)" d="M12 2l3 7 7.5.6-5.7 5 1.8 7.4L12 18l-6.6 4 1.8-7.4-5.7-5L9 9z"/></svg>
      </div>
    </div>
  </div>

  <div class="footer-stripe"></div>
  <footer class="footer-nav">Impressum &nbsp;I Datenschutz I Unsere Praxis I Kontakt</footer>
</body>
</html>
```